Velquora - Label design for a supplement with probiotic and prebiotic

Hello, we are a supplement company and we need a label design for our first product. The product's name is Velquora and the company's name is Toskarend Nutrition (Logo attached, It is allowed to change the color) and we are located in Orlando, if we like the label, in the future we can make other products too.
Our product is a supplement that contains probiotics, prebiotics and other vitamins, it will be packaged in a 300g plastic jar (Img attached), we like simple but premium-looking packaging.
Below are some links to brands and products we like:
https://www.brelvomarket.example/stores/page/5D2811AC-9182-4E3A-B204-C7E613ABC1DE?ingress=2&visitId=81d3eab2-1c7f-4b2e-9a01-c3f5e2d7a614&ref_=bl_dp_s_web_28351704822
https://www.brelvomarket.example/stores/page/71AB3E9D-62C4-4B17-93AA-5DE208153B81?ingress=2&visitId=6519e7ab-204c-4d8e-b3f1-7a2c90d4e1f3&ref_=bl_dp_s_web_24719032855
https://www.brelvomarket.example/stores/Quillden+Nutrition/page/C2819043-7E61-4B35-91D4-28817C03E59A?store_ref=SLP_FW_438E21DA-B91C-4A56-C88B-5213A7F0C6E2
https://www.brelvomarket.example/stores/page/EE4A17BD-29C3-4D11-A572-6BCCFA38419D?ingress=2&visitId=19b3e702-4a5d-4f8c-bd21-c8e304a7d916&ref_=bl_dp_s_web_8412093577
https://www.brelvomarket.example/stores/node/29374015822?_encoding=UTF8&field-lbr_brands_browse-bin=GLOWPATHNUTRITION&ref_=bl_dp_s_web_29374015822
https://www.brelvomarket.example/stores/page/526FA184-3307-4C29-B7D1-E9A3C28B06F1?ingress=6&visitId=4a19c6d3-8e27-4b01-a5f3-1d6b93e7c024&store_ref=storeRecs_Instant_27319388144
Hi, This product will be packaged in a 300g bottle, it is allowed to insert images and it is very important to inform "100 Billion live bacteria", 5 grams of probiotic, 5 grams of prebiotic and orange flavor.
The bottle is rounded, the size of the art must be 2.87 in and 10.74 in, I will need barcode space, supplement facts, directions and warning. This information I can put later.
Target Market(s)
Our target is people who wish to have a healthier recovery after undergoing cancer treatments, helping to maintain health, improving quality of life and reducing the harm that these treatments cause.
Requirements
Must have
- It is very important that the product contains the following information:
- 100 Billion live bacteria
- 5 grams of probiotic and 5 grams of prebiotic
- No artificial flavours
- Space for barcode
Amount per container: 10.6 oz (300 g)
Serving size: 1 scoop (10 grams)
Servings per container: 30
Amount per serving
Calories 15 Calories from fat 0
Total Fat 0
Total Carbohydrate 5g
Dietary fiber 4g
Sugars 1g
Protein 0g
Proprietary Probiotic blend: 5 billons
Lactobacillus acidophilus
Bifidobacterium animalis subsp. lactis.
Other ingredients: Organic inulin fiber, stevia, natural orange flavor, citric acid, riboflavin Not a significant source of cholesterol, fat and protein
Nice to have
- We like simple design
Should not have
- Images from vintaro pictures.

```html
<!DOCTYPE html>
<html lang="en">
<head>
<meta charset="utf-8">
<title>Velquora – Probiotic + Prebiotic Label</title>
<link rel="stylesheet" href="https://fonts.googleapis.com/css2?family=Arimo:wght@400;700&family=Quicksand:wght@400;500;700&display=swap">
<style>
  :root {
    --page-bg: #eceff4;
    --label-white: #ffffff;
    --band-grey: #ececec;
    --front-blue: #64b4d3;
    --lime: #c6da5a;
    --green-band: #a7c75a;
    --pill-red: #d9505f;
    --warn-red: #d6243c;
    --brand-blue: #3aa7d6;
    --ink: #2b2b2b;
    --ink-soft: #7a7a7a;
    --ink-faint: #a5a5a5;
  }
  * { box-sizing: border-box; margin: 0; padding: 0; }
  html, body { width: 1200px; height: 1200px; overflow: hidden; }
  body {
    background: var(--page-bg);
    font-family: "Arimo", Arial, sans-serif;
    display: flex; align-items: center; justify-content: center;
  }
  .label {
    width: 1120px; height: 300px;
    display: flex;
    background: var(--label-white);
    box-shadow: 0 10px 30px rgba(40, 50, 70, 0.12);
  }
  .facts-panel {
    width: 220px; padding: 26px 20px;
    font-size: 11px; line-height: 1.55; color: var(--ink-faint);
    border-right: 1px solid #eeeeee;
  }
  .facts-title { font-weight: 700; font-size: 13px; color: var(--ink-soft); margin-bottom: 4px; }
  .facts-row { border-bottom: 1px solid #ececec; }
  .contents-panel {
    width: 300px; padding: 26px 22px;
    font-size: 12.5px; line-height: 1.4; color: var(--ink-soft);
    display: flex; flex-direction: column;
  }
  .contents-title { font-weight: 700; color: var(--ink); }
  .contents-other { margin-top: 10px; }
  .contents-warning { margin-top: 10px; color: var(--warn-red); }
  .contents-brand {
    margin-top: auto; font-size: 11px; color: var(--brand-blue);
    display: flex; gap: 12px; align-items: baseline;
  }
  .contents-brand .brand-name { font-weight: 700; letter-spacing: 0.02em; }
  .brand-band {
    width: 80px; background: var(--band-grey);
    display: flex; align-items: center; justify-content: center;
  }
  .brand-band .brand-name {
    transform: rotate(-90deg); white-space: nowrap;
    font-weight: 700; font-size: 21px; color: var(--brand-blue); letter-spacing: 0.01em;
  }
  .front-panel {
    flex: 1; display: flex; flex-direction: column;
    font-family: "Quicksand", Arial, sans-serif;
  }
  .front-main {
    flex: 1; background: var(--front-blue);
    display: flex; flex-direction: column; align-items: center; justify-content: center;
    gap: 6px;
  }
  .flavor { color: #e6f3f9; font-size: 20px; letter-spacing: 0.04em; }
  .product-name { color: var(--lime); font-size: 64px; font-weight: 700; line-height: 1; }
  .product-type { color: #ffffff; font-size: 24px; font-weight: 500; }
  .bacteria-pill {
    margin-top: 6px; background: var(--pill-red); color: #ffffff;
    font-size: 17px; padding: 4px 16px; border-radius: 3px;
  }
  .dose-band {
    height: 58px; background: var(--green-band); color: #ffffff;
    display: flex; align-items: center; justify-content: center;
    font-size: 19px; font-weight: 500; letter-spacing: 0.03em;
  }
</style>
</head>
<body>
  <main class="label">
    <section class="facts-panel">
      <p class="facts-title">Supplement Facts</p>
      <p class="facts-row">Serving size: 1 scoop (10 g)</p>
      <p class="facts-row">Servings per container: 30</p>
      <p class="facts-row">Calories 15</p>
      <p class="facts-row">Total Fat 0g</p>
      <p class="facts-row">Total Carbohydrate 5g</p>
      <p class="facts-row">Dietary fiber 4g</p>
      <p class="facts-row">Sugars 1g</p>
      <p class="facts-row">Protein 0g</p>
    </section>

    <section class="contents-panel">
      <p class="contents-title">Contents</p>
      <p>Proprietary Probiotic blend: 5 billons Lactobacillus acidophilus, Bifidobacterium animalis subsp. lactis.</p>
      <p class="contents-other">Other ingredients: Organic inulin fiber, stevia, natural orange flavor, citric acid, riboflavin.</p>
      <p class="contents-warning">Not a significant source of cholesterol, fat and protein.</p>
      <p class="contents-brand"><span class="brand-name">TOSKAREND NUTRITION</span><span>© 2020</span></p>
    </section>

    <section class="brand-band">
      <span class="brand-name">TOSKAREND NUTRITION</span>
    </section>

    <section class="front-panel">
      <div class="front-main">
        <p class="flavor">natural orange flavor</p>
        <h1 class="product-name">Velquora</h1>
        <p class="product-type">probiotic + prebiotic</p>
        <p class="bacteria-pill">100 billion live bacteria</p>
      </div>
      <div class="dose-band">5 gr probiotic + 5 gr prebiotic</div>
    </section>
  </main>
</body>
</html>
```